KT Holdings Company brochure

require the design of a brochure for my company KT holdings which incorporates 2 separate companies specialising in home technology and security. Im not sure whether its going to be best to do one brochure with all the info in or 2 individual ones

Target Market(s)

Footballers and High net worth individuals

Industry/Entity Type

Information Technology

Font styles to use
Serif
Other font styles liked:
• Neuropol (this is the logo font)

Colors
ec1f27
000000
9d9d9d

Requirements
Must have
• 2 sections one for audio visual and 1 for security

```html
<!DOCTYPE html>
<html lang="en">
<head>
<meta charset="utf-8">
<title>KT Holdings Brochure</title>
<link href="https://fonts.googleapis.com/css2?family=Michroma&family=Open+Sans:wght@400;600&display=swap" rel="stylesheet">
<style>
  :root {
    --red: #ec1f27;
    --black: #000000;
    --grey: #9d9d9d;
    --backdrop: #dcdcdc;
    --panel-light: #f4f4f4;
    --panel-mid: #d9d9d9;
    --ink: #222222;
    --paper-ink: #e6e6e6;
  }
  * { box-sizing: border-box; margin: 0; padding: 0; }
  html, body { width: 1009px; height: 1200px; overflow: hidden; }
  body {
    background: var(--backdrop);
    font-family: "Open Sans", sans-serif;
    color: var(--ink);
    position: relative;
  }
  .spread {
    position: absolute;
    left: 34px;
    width: 940px;
    height: 540px;
    display: flex;
  }
  .spread--tech { top: 30px; }
  .spread--security { top: 630px; }
  .page {
    width: 470px;
    height: 540px;
    background: var(--black);
    padding: 16px;
    display: flex;
  }
  .page + .page { border-left: 1px solid #2a2a2a; }
  .panel {
    flex: 1;
    background: linear-gradient(160deg, var(--panel-light), var(--panel-mid));
    border-radius: 4px;
    display: flex;
    flex-direction: column;
    overflow: hidden;
  }
  .photos {
    display: flex;
    gap: 6px;
    height: 180px;
    background: var(--black);
    padding-bottom: 6px;
  }
  .photo { flex: 1; }
  .photo--control-room { background: linear-gradient(135deg, #3a0b0b, #c2341f 55%, #1a1a1a); }
  .photo--interior { background: linear-gradient(135deg, #f2f2f2, #bdbdbd); }
  .photo--thermostat { background: linear-gradient(135deg, #2b2b2b, #c8c8c8 60%, #d8b49a); }
  .photo--pool { background: linear-gradient(160deg, #5f6e72, #2fa6b4 65%, #38281e); }
  .photo--keypad { background: linear-gradient(135deg, #dcdcdc, #23262c 45%, #5a6f86); }
  .photo--door-app { background: linear-gradient(135deg, #ffffff, #e9e9e9 40%, #2a2a2a 70%, #ffffff); }
  .content {
    flex: 1;
    padding: 22px 24px 20px;
    border-top: 5px solid var(--black);
    border-top-left-radius: 50% 24px;
    border-top-right-radius: 50% 24px;
    margin-top: -4px;
    background: inherit;
  }
  .heading {
    font-family: "Michroma", sans-serif;
    font-size: 15px;
    font-weight: 400;
    color: var(--black);
    margin-bottom: 12px;
    letter-spacing: 0.2px;
  }
  .heading .accent { color: var(--red); }
  .body-copy { font-size: 9.5px; line-height: 1.5; margin-bottom: 12px; }
  .features { list-style: disc; padding-left: 14px; font-size: 9.5px; line-height: 1.55; }
  .divider { height: 5px; background: var(--black); margin: 14px -24px; }
  .page--intro .panel {
    background: radial-gradient(ellipse at 50% 20%, #2e2e2e, var(--black) 70%);
    color: var(--paper-ink);
    padding: 60px 40px 30px;
    align-items: center;
  }
  .brand {
    display: flex;
    align-items: center;
    gap: 10px;
    margin-bottom: 40px;
  }
  .brand-dot { width: 22px; height: 22px; border-radius: 50%; background: var(--red); }
  .brand-name { font-family: "Open Sans", sans-serif; font-weight: 600; font-size: 17px; color: var(--paper-ink); }
  .intro-copy { font-size: 10px; line-height: 1.6; margin-bottom: 12px; }
</style>
</head>
<body>

<section class="spread spread--tech">
  <article class="page">
    <div class="panel">
      <div class="photos">
        <div class="photo photo--control-room" role="img" aria-label="Photo of a media control room with red desks and wall screens"></div>
        <div class="photo photo--interior" role="img" aria-label="Photo of a bright interior with a wall-mounted touch panel"></div>
      </div>
      <div class="content">
        <h2 class="heading">Communications/ <span class="accent">Broadband Networks</span></h2>
        <p class="body-copy">It has always been our belief that whatever technology is being used to run a business, it is completely reliant on the very network platform it sits on. Halden Technologies is dedicated in providing customers with the right network platforms to underpin their business requirements and form the core of our solution designs. Whether it is voice, data or video we aim to look further than the immediate requirement to ensure that the solutions we implement now will support the applications of the future.</p>
        <ul class="features">
          <li>Data networking – a solid infrastructure for now and the future</li>
          <li>“Designed in” robustness and security</li>
          <li>Reliable Wi-Fi network in all areas of the house including garden (if required)</li>
          <li>Analogue, Digital and SIP “cloud” based phone systems</li>
          <li>In house expertise on file sharing, secure backups, equipment synchronizing and “cloud” based solutions</li>
          <li>Supply of dedicated fiber optic leased line connections up to 1GB guaranteed</li>
          <li>Mobile phone signal boosting</li>
        </ul>
      </div>
    </div>
  </article>
  <article class="page">
    <div class="panel">
      <div class="photos">
        <div class="photo photo--thermostat" role="img" aria-label="Photo of a smart thermostat and a phone climate app"></div>
        <div class="photo photo--pool" role="img" aria-label="Photo of an indoor swimming pool"></div>
      </div>
      <div class="content">
        <h2 class="heading">Climate Control/ <span class="accent">Renewable Energy</span></h2>
        <p class="body-copy">We understand that energy and carbon saving are high on the agenda for businesses today. We have a range of offerings to allow building owners/occupiers to control, monitor and manage their actual energy usage and compare this to required values. We can assist in designing, specifying and supplying the latest integrated technology for tomorrow’s buildings encompassing such areas as lighting, energy efficiency, heating, ventilation and air conditioning control. The requirements placed on building services plant are becoming more complex and there is an increased demand for standardised communication. As a result, our comprehensive offering is based on international standards and state of the art technologies including BACNet and KNX.</p>
        <ul class="features">
          <li>Combining internal and external sensors provides “intelligent” control that reduces energy consumption</li>
          <li>View and manage energy usage on your control interface</li>
          <li>Integrate and manage micro generation information</li>
          <li>Solar power, wind turbines and hydro generation can all be accommodated</li>
        </ul>
      </div>
    </div>
  </article>
</section>

<section class="spread spread--security">
  <article class="page page--intro">
    <div class="panel">
      <div class="brand">
        <span class="brand-dot"></span>
        <span class="brand-name">Halden Protection Solutions</span>
      </div>
      <p class="intro-copy">Halden Protection Solutions is the security arm of KT Holdings. At Halden Protection Solutions we look after your business by delivering high quality (TBSM) Total Building Security &amp; Management solutions. We are specialists in traditional and IP-based Access Control, CCTV and Building Management Systems. We take advantage of the advances in security, IP management and surveillance technology to get the best out new devices and software, and minimize any risks and costs to your business.</p>
      <p class="intro-copy">With our Groups combined expertise, we can easily integrate with existing or new IT infrastructure or Audio / Visual systems to provide a complete building wide portfolio of services to manage, secure and evolve your building so that it meets the legislation constraints for carbon foot print and sustainability, ease of access for the occupants and visitors and above all the security that your business demands.</p>
      <p class="intro-copy">From single devices to complex, integrated systems, each project is unique to you and your business and is given due care and attention to ensure that you are fully protected with the highest level of system monitoring whilst minimizing the costs of managing your building infrastructure.</p>
    </div>
  </article>
  <article class="page">
    <div class="panel">
      <div class="photos">
        <div class="photo photo--keypad" role="img" aria-label="Photo of an alarm control keypad"></div>
        <div class="photo photo--door-app" role="img" aria-label="Photo of a hand holding a smartphone showing a front door video call"></div>
      </div>
      <div class="content">
        <h2 class="heading">CCTV/ <span class="accent">Security</span></h2>
        <ul class="features">
          <li>Personal reassurance while you are at home and confidence when you are away</li>
          <li>Access images remotely on all your devices, where ever you are in the world</li>
          <li>High definition IP cameras giving evidence grade recordings</li>
          <li>Alarms installed and certified upto grade 1 response category with two way audio</li>
        </ul>
        <div class="divider"></div>
        <h2 class="heading">Access <span class="accent">Control</span></h2>
        <ul class="features">
          <li>Video and audio door entry to keep your property secure</li>
          <li>Control from your tablet, smartphone, dedicated wireless handsets and wall units</li>
          <li>“Frictionless” access for trusted individuals or vehicles via RFID, biometrics and PIN codes</li>
          <li>Automation of gates and barriers</li>
        </ul>
      </div>
    </div>
  </article>
</section>

</body>
</html>
```